TBrenwick Business Cards & Letterhead

I have a logo but need a design for some new business cards. We are a Design-Build Firm that specializes in the design and construction of commercial projects.
the cards need to be professional. no cartoon stuff.
i would like to have the cards in AI format so I can update the card as needed. Logo is provided.
Our Address is: 4718 Fenmoor Ct. Brackenford, North Carolina 27500

```html
<!DOCTYPE html>
<html lang="en">
<head>
<meta charset="utf-8">
<title>TBrenwick Business Card</title>
<link rel="stylesheet" href="https://fonts.googleapis.com/css2?family=Open+Sans:wght@400;600;700;800&display=swap">
<style>
  :root {
    --stage: #333333;
    --card-dark: #202024;
    --blue-light: #1a80c4;
    --blue-deep: #0a385f;
    --blue-text: #1b74b8;
    --brand-grey: #7d7d82;
    --emboss-blue: #0c446f;
    --emboss-dark: #141417;
    --white: #f4f4f4;
  }
  * { margin: 0; padding: 0; box-sizing: border-box; }
  html, body { width: 1200px; height: 780px; overflow: hidden; }
  body {
    background: var(--stage);
    font-family: "Open Sans", Arial, sans-serif;
    position: relative;
  }
  .card {
    position: absolute;
    width: 560px;
    height: 320px;
    overflow: hidden;
    box-shadow: 0 10px 24px rgba(0,0,0,0.45);
  }
  .card-front {
    left: 50px; top: 70px;
    background: radial-gradient(ellipse at 50% 55%, var(--blue-light) 0%, #125d95 45%, var(--blue-deep) 100%);
    display: flex; align-items: center; justify-content: center;
  }
  .front-brand {
    font-weight: 800;
    font-size: 64px;
    letter-spacing: 3px;
    color: var(--emboss-blue);
  }
  .card-back {
    left: 590px; top: 390px;
    background: var(--card-dark);
  }
  .brand {
    position: absolute; left: 34px; top: 34px;
    display: flex; align-items: center; gap: 10px;
  }
  .brand-square { width: 22px; height: 22px; background: var(--blue-text); }
  .brand-name {
    font-weight: 800; font-size: 34px; letter-spacing: 1px;
    color: var(--brand-grey);
  }
  .accent-bar {
    position: absolute; left: 30px; top: 138px;
    width: 10px; height: 48px;
    background: linear-gradient(180deg, #0d5d9c, var(--blue-light));
  }
  .person { position: absolute; left: 52px; top: 130px; }
  .person-name {
    font-weight: 700; font-size: 24px; letter-spacing: 1px;
    color: var(--blue-text); line-height: 1.15;
  }
  .person-title { font-weight: 600; font-size: 15px; color: var(--white); }
  .address {
    position: absolute; left: 60px; top: 198px;
    font-size: 14px; line-height: 1.3; color: var(--white);
  }
  .contacts {
    position: absolute; left: 60px; top: 244px;
    list-style: none; font-size: 14px; line-height: 1.4; color: var(--white);
  }
  .contacts li { display: flex; align-items: center; gap: 8px; }
  .contacts svg { width: 12px; height: 12px; fill: var(--blue-text); flex: none; }
  .side-brand {
    position: absolute; right: -118px; top: 142px;
    transform: rotate(90deg);
    font-weight: 800; font-size: 40px; letter-spacing: 2px;
    color: var(--emboss-dark);
    white-space: nowrap;
  }
</style>
</head>
<body>
  <section class="card card-front" aria-label="Card front">
    <span class="front-brand">TBRENWICK</span>
  </section>

  <section class="card card-back" aria-label="Card back">
    <div class="brand">
      <span class="brand-square"></span>
      <span class="brand-name">TBRENWICK</span>
    </div>
    <span class="accent-bar"></span>
    <div class="person">
      <p class="person-name">MARCUS BRENWICK</p>
      <p class="person-title">Founder/President</p>
    </div>
    <p class="address">4718 Fenmoor Ct. Brackenford,<br>North Carolina 27500</p>
    <ul class="contacts">
      <li><svg viewBox="0 0 24 24"><path d="M6.6 10.8a15 15 0 0 0 6.6 6.6l2.2-2.2c.3-.3.7-.4 1-.2 1.1.4 2.3.6 3.6.6.6 0 1 .4 1 1V20c0 .6-.4 1-1 1A17 17 0 0 1 3 4c0-.6.4-1 1-1h3.5c.6 0 1 .4 1 1 0 1.3.2 2.5.6 3.6.1.3 0 .7-.2 1z"/></svg>(919) 555-0148</li>
      <li><svg viewBox="0 0 24 24"><circle cx="12" cy="12" r="10"/></svg>www.tbrenwick.com</li>
      <li><svg viewBox="0 0 24 24"><path d="M2 5h20v14H2z"/></svg>MAB@TBrenwick.com</li>
    </ul>
    <span class="side-brand">TBRENWICK</span>
  </section>
</body>
</html>
```